Media Company's Events Website Needs a Design

International Media Company is setting up a new website to market own and partners' events in the Asia Pacific region.

The sitemap and sections are described in the attached document. Supporting images, logos and layout for the mockups are also provided.

We require design mockups for 4 key pages. Please submit homepage mockup for evaluation first. We will give the go-ahead for the other 3 pages once your homepage design is approved, so you do not have to waste unnecessary time.

Any question which I did not cover, please email milo+artpanel@brightvane.example. Thanks!
Updates

Hi all designers, our client has decided to simplify the website, dropping 2 event categories and focusing on just 1 (i.e. Vivid Pathways). 

I am uploading a new homepage layout doc. 

Specifically, changes are:
- New set of tabs on the main menu
- Content area will include: (i) testimonial slider; (ii) video block; (iii) list of upcoming events. feel free to play around with the layout.

Thanks and sorry for the trouble!
Milo

Hi all designers, I have re-uploaded the new brief with respect to the section changes.

Please download and refer to the changes.

Thanks!

Target Market(s)

Corporations, Businessmen, C-level Executives

Industry/Entity Type

Events

Requirements
Must have
• Refer to layout document
Nice to have
• The website may be implemented using WordPress, so a typical 1- and 2-column layout would be deployment-friendly.

```html
<!DOCTYPE html>
<html lang="en">
<head>
<meta charset="utf-8">
<title>Vivid Pathways – Events</title>
<link href="https://fonts.googleapis.com/css2?family=Arimo:wght@400;700&family=Tinos:wght@700&display=swap" rel="stylesheet">
<style>
:root{
  --sky:#2f93cf;
  --nav-border:#1d6fa4;
  --navy:#1b3f5e;
  --navy-deep:#163650;
  --band:#ebebeb;
  --ink:#333;
  --ink-soft:#555;
  --quote-blue:#1f6aa8;
  --title-blue:#1d6aa5;
  --accent-red:#c8141b;
  --green:#3a7d12;
  --white:#fff;
}
*{box-sizing:border-box;margin:0;padding:0}
html,body{width:1049px;height:1200px;overflow:hidden}
body{position:relative;background:var(--white);font-family:Arimo,Arial,sans-serif;color:var(--ink)}
.abs{position:absolute}

/* header */
.site-header{left:0;top:0;width:1049px;height:118px;background:radial-gradient(ellipse at 290px 40px,#5bb4e6 0%,var(--sky) 45%,#2a8ac6 100%)}
.brand{left:148px;top:24px;display:flex;align-items:center;gap:10px}
.brand-name{font-size:34px;font-weight:400;color:#5a5a5a;letter-spacing:-0.5px}
.brand-dot{width:14px;height:14px;border-radius:50%;background:#5a5a5a}
.account{left:810px;top:0;width:92px;height:22px;background:var(--navy-deep);color:var(--white);font-size:11px;line-height:22px;text-align:center}
.main-nav{left:148px;top:84px;width:754px;height:34px;display:flex;border:1px solid var(--nav-border);border-bottom:none}
.main-nav a{display:block;height:33px;line-height:33px;text-align:center;color:var(--white);font-size:12px;text-decoration:none;border-right:1px solid var(--nav-border);white-space:nowrap}
.main-nav a:last-child{border-right:none}
.main-nav a.active{background:var(--navy)}

/* testimonial */
.testimonial{left:0;top:118px;width:1049px;height:296px;background:var(--band);border-bottom:2px solid #cfcfcf}
.speaker-photo{left:202px;top:25px;width:213px;height:248px;border:3px solid var(--white);background:linear-gradient(160deg,#8a6a45,#3b2d22 60%,#1e1e22);box-shadow:0 6px 10px rgba(0,0,0,.25)}
.slide-arrow{top:113px;width:36px;height:36px}
.quote-mark{left:448px;top:38px;font-family:Tinos,serif;font-weight:700;font-size:92px;line-height:1;color:#444}
.quote-text{left:468px;top:64px;width:404px;font-size:18px;line-height:21.7px;color:var(--quote-blue);text-indent:36px;hyphens:auto;-webkit-hyphens:auto}
.quote-rule{left:468px;top:190px;width:402px;border-top:1px dotted #777}
.quote-author{left:468px;top:204px;font-size:20px;line-height:24px;color:#333;white-space:nowrap}
.quote-author span{color:var(--accent-red)}

/* video */
.video-block{left:150px;top:455px;width:498px;height:288px;background:linear-gradient(180deg,#e8e2d8 0%,#c9a46a 30%,#7a5a3a 65%,#2c2622 100%)}
.play{left:214px;top:90px}
.video-caption{left:0;bottom:0;width:498px;height:67px;background:rgba(30,30,30,.78);padding:10px 20px;color:var(--white)}
.video-caption h3{font-size:16px;font-weight:400;margin-bottom:4px;white-space:nowrap}
.video-caption p{font-size:10px;line-height:12px;color:#ddd}

/* about */
.about-title{left:150px;top:780px;font-size:18.5px;font-weight:400;color:#333}
.about-photo{left:148px;top:812px;width:180px;height:144px;border:1px solid #ccc;padding:4px;background:var(--white)}
.about-photo div{width:100%;height:100%;background:linear-gradient(160deg,#e6d4bc,#b98a5c 45%,#3a3430)}
.about-text{left:337px;top:812px;width:312px;font-size:11.3px;line-height:13.6px;color:var(--ink-soft);text-align:justify}
.about-text p+p{margin-top:8px}

/* events */
.events-title{left:693px;top:452px;font-size:18.5px;font-weight:400;color:#333}
.event{left:693px;width:209px;height:112px}
.event-name{position:absolute;left:1px;top:0;font-size:13px;font-weight:700;color:var(--title-blue);white-space:nowrap}
.cal{position:absolute;left:1px;top:13px;width:52px;height:58px}
.cal-month{position:absolute;left:3px;width:48px;height:13px;background:#a3191d;color:var(--white);font-size:9px;line-height:13px;text-align:center}
.cal-day{position:absolute;left:3px;width:48px;text-align:center;font-family:Tinos,serif;font-weight:700;font-size:22px;color:#444}
.event-city{position:absolute;left:63px;top:18px;font-size:16px;font-weight:700;color:#111;white-space:nowrap}
.event-link{position:absolute;left:65px;font-size:14.5px;white-space:nowrap}
.more{top:40px;color:var(--green)}
.attend{top:59px;color:var(--accent-red)}
.event-rule{position:absolute;left:0;top:87px;width:209px;border-top:1px dotted #777}
.calendar-btn{left:693px;top:926px;width:209px;height:30px;background:linear-gradient(#3a8ccb,#1d5f97);color:var(--white);font-size:15px;line-height:30px;text-align:center}

/* footer */
.site-footer{left:0;top:1023px;width:1049px;height:177px;background:var(--navy)}
.f-col{top:18px}
.f-col h4{font-size:12px;font-weight:400;color:var(--white);margin-bottom:14px;white-space:nowrap}
.f-col a{display:block;font-size:10.5px;color:#dfe8ef;text-decoration:none;line-height:19.5px;white-space:nowrap}
.newsletter p{width:210px;font-size:10.5px;line-height:12px;color:#dfe8ef;margin-top:-4px}
.signup{display:flex;margin-top:10px;width:209px;height:22px}
.signup span{flex:1;background:var(--navy-deep);color:#ddd;font-size:12px;line-height:22px;padding-left:7px}
.signup b{width:57px;background:#b5161c;color:var(--white);font-weight:400;font-size:12px;line-height:22px;text-align:center}
.f-rule{left:148px;top:131px;width:754px;border-top:1px solid #2f5a7c}
.copyright{left:148px;top:141px;font-size:10.5px;color:#dfe8ef}
</style>
</head>
<body>

<header class="site-header abs">
  <div class="brand abs"><span class="brand-name">Vivid Pathways</span><span class="brand-dot"></span></div>
  <div class="account abs">Login &nbsp;|&nbsp; Register</div>
  <nav class="main-nav abs">
    <a style="width:73px">Home</a>
    <a style="width:175px">About Vivid Pathways</a>
    <a style="width:137px">Upcoming Events</a>
    <a style="width:111px" class="active">Past Events</a>
    <a style="width:83px">Videos</a>
    <a style="flex:1">Partnership Opportunities</a>
  </nav>
</header>

<section class="testimonial abs">
  <div class="speaker-photo abs" role="img" aria-label="Photo of the speaker presenting with a microphone"></div>
  <svg class="slide-arrow abs" style="left:125px" viewBox="0 0 36 36"><circle cx="18" cy="18" r="18" fill="#6a6a6a"/><path d="M22 10 L11 18 L22 26Z" fill="#fff"/></svg>
  <svg class="slide-arrow abs" style="left:888px" viewBox="0 0 36 36"><circle cx="18" cy="18" r="18" fill="#6a6a6a"/><path d="M14 10 L25 18 L14 26Z" fill="#fff"/></svg>
  <div class="quote-mark abs">&ldquo;</div>
  <p class="quote-text abs">What’s great about Hangzhou and having officials from the city come to San Francisco to share their ideas, we learn a lot about IP protection, about their real investment in making it a really clean and global city.</p>
  <div class="quote-rule abs"></div>
  <p class="quote-author abs">Daniel Hartley, Chief Commercial Officer,<br><span>Brightfield Energy</span></p>
</section>

<div class="video-block abs" role="img" aria-label="Video still of a panel discussion on stage before a seated audience">
  <svg class="play abs" width="72" height="72" viewBox="0 0 72 72"><circle cx="36" cy="36" r="34" fill="#1a5fb0" stroke="#dfe9f5" stroke-width="4"/><path d="M28 21 L52 36 L28 51Z" fill="#fff"/></svg>
  <div class="video-caption abs">
    <h3>Lorem ipsum dolor sit amet, consectetur adipiscing elit</h3>
    <p>Lorem ipsum dolor sit amet, consectetur adipiscing elit. Praesent in varius nulla. Vivamus ullamcorper neque quis diam gravida vel lobortis nulla mollis.</p>
  </div>
</div>

<h2 class="about-title abs">About Vivid Pathways</h2>
<div class="about-photo abs"><div role="img" aria-label="Photo of panelists seated on a conference stage"></div></div>
<div class="about-text abs">
  <p>Meridian Asia’s newly formed “Vivid Pathways” team, based in Singapore, offers clients customized and integrated on air and on –ground turn – key 360 solutions, tailored to client’s objectives, allowing for closer integrated brand messaging.</p>
  <p>Providing bespoke events where specific topics and issues are disussed either with a panel of experts or in roundtables with other industry stakeholders. Co – branded between the client and Meridian Vivid Pathways, the whole look and feel of the event from beginning to end, concept and execution will be designed with the clients branding and messaging in mind.</p>
</div>

<h2 class="events-title abs">Upcoming Events</h2>

<article class="event abs" style="top:490px">
  <div class="event-name">INSIDE CHINA’S FUTURE</div>
  <svg class="cal" viewBox="0 0 52 58"><rect x="3" y="6" width="48" height="50" fill="#e6e6e6" stroke="#bbb"/><g stroke="#666" stroke-width="1.2"><path d="M7 3v6M12 3v6M17 3v6M22 3v6M27 3v6M32 3v6M37 3v6M42 3v6M47 3v6"/></g></svg>
  <div class="cal-month" style="top:21px">September</div>
  <div class="cal-day" style="top:37px">12</div>
  <div class="event-city">Tianjin, China</div>
  <div class="event-link more">Find out more</div>
  <div class="event-link attend">Attend the event</div>
  <div class="event-rule"></div>
</article>

<article class="event abs" style="top:602px">
  <div class="event-name">ENERGY-NEXT ASIA</div>
  <svg class="cal" viewBox="0 0 52 58"><rect x="3" y="6" width="48" height="50" fill="#e6e6e6" stroke="#bbb"/><g stroke="#666" stroke-width="1.2"><path d="M7 3v6M12 3v6M17 3v6M22 3v6M27 3v6M32 3v6M37 3v6M42 3v6M47 3v6"/></g></svg>
  <div class="cal-month" style="top:21px">October</div>
  <div class="cal-day" style="top:37px">3-5</div>
  <div class="event-city">Bangkok, Thailand</div>
  <div class="event-link more">Find out more</div>
  <div class="event-link attend">Attend the event</div>
  <div class="event-rule"></div>
</article>

<article class="event abs" style="top:712px">
  <div class="event-name">INSIDE CHINA’S FUTURE</div>
  <svg class="cal" viewBox="0 0 52 58"><rect x="3" y="6" width="48" height="50" fill="#e6e6e6" stroke="#bbb"/><g stroke="#666" stroke-width="1.2"><path d="M7 3v6M12 3v6M17 3v6M22 3v6M27 3v6M32 3v6M37 3v6M42 3v6M47 3v6"/></g></svg>
  <div class="cal-month" style="top:21px">September</div>
  <div class="cal-day" style="top:37px">12</div>
  <div class="event-city">Tianjin, China</div>
  <div class="event-link more">Find out more</div>
  <div class="event-link attend">Attend the event</div>
  <div class="event-rule"></div>
</article>

<article class="event abs" style="top:824px">
  <div class="event-name">ENERGY-NEXT ASIA</div>
  <svg class="cal" viewBox="0 0 52 58"><rect x="3" y="6" width="48" height="50" fill="#e6e6e6" stroke="#bbb"/><g stroke="#666" stroke-width="1.2"><path d="M7 3v6M12 3v6M17 3v6M22 3v6M27 3v6M32 3v6M37 3v6M42 3v6M47 3v6"/></g></svg>
  <div class="cal-month" style="top:21px">October</div>
  <div class="cal-day" style="top:37px">3-5</div>
  <div class="event-city">Bangkok, Thailand</div>
  <div class="event-link more">Find out more</div>
  <div class="event-link attend">Attend the event</div>
</article>

<div class="calendar-btn abs">See Full Calendar</div>

<footer class="site-footer abs">
  <div class="f-col abs" style="left:148px"><h4>Events</h4><a>Strategic Events</a><a>Vivid Pathways</a><a>Partner Events</a></div>
  <div class="f-col abs" style="left:296px"><h4>Join Us</h4><a>Login</a><a>Register</a></div>
  <div class="f-col abs" style="left:416px"><h4>Connect with us</h4><a>Circlepage</a><a>Chirpline</a><a>Workmesh</a></div>
  <div class="f-col abs" style="left:568px"><h4>Help</h4><a>Contact us</a><a>Privacy Policy</a><a>Sitemap</a></div>
  <div class="f-col newsletter abs" style="left:694px"><h4>Newsletter Signup</h4>
    <p>Lorem ipsum dolor sit amet, consectetur adipiscing elit. Integer quis libero nisi.</p>
    <div class="signup"><span>your email</span><b>signup</b></div>
  </div>
  <div class="f-rule abs"></div>
  <div class="copyright abs">Copyright © 2012 Vivid Pathways. All Right Reserved</div>
</footer>

</body>
</html>
```